Letterhead and Envelope Design for Investment Company

We need a letterhead and envelope design.
We are a family owned investment company doing direct investments into other family owned businesses.
I have attached all our current marketing material including our logo for reference.

Our under construction website can be found here:
https://rob-darke-qv7m.pagevorlo.com/
password: Copperfen

Target Market(s)

Bankers, business owners, financial partners

Industry/Entity Type

Investment

Colors

Designer to choose colors to be used in the design.

Requirements
Must have
• Logo, and company information

```html
<!DOCTYPE html>
<html lang="en">
<head>
<meta charset="utf-8">
<title>Copperfen Holdings – Stationery</title>
<link href="https://fonts.googleapis.com/css2?family=Didact+Gothic&display=swap" rel="stylesheet">
<style>
  :root{
    --backdrop:#d3d3d3;
    --charcoal:#3a3a3a;
    --paper:#f3f3f3;
    --gold:#c9971f;
    --ink:#2b2b2b;
    --muted:#9a9a9a;
  }
  *{margin:0;padding:0;box-sizing:border-box}
  html,body{width:1200px;height:1051px;overflow:hidden}
  body{background:var(--backdrop);font-family:"Didact Gothic",sans-serif;color:var(--ink);position:relative}
  .piece{position:absolute;background:var(--paper)}
  .wordmark{position:absolute;font-family:"Didact Gothic",sans-serif;color:var(--ink);letter-spacing:.06em;white-space:nowrap;text-transform:uppercase}

  /* folder */
  .folder{left:165px;top:91px;width:419px;height:541px;background:var(--charcoal);border-radius:3px}
  .folder-spine{position:absolute;left:27px;top:0;bottom:0;width:2px;background:#2c2c2c}
  .folder .wordmark{left:0;right:0;top:128px;text-align:center;font-size:22px;color:var(--gold)}

  /* letterhead */
  .letterhead{left:615px;top:110px;width:404px;height:522px}
  .header-band{position:absolute;left:0;top:0;width:100%;height:30px}
  .letterhead .wordmark{left:38px;top:64px;font-size:11px}
  .letter-body{position:absolute;left:38px;top:115px;width:330px;font-size:5.4px;line-height:1.3;text-align:justify}
  .letter-date{margin-bottom:9px}
  .recipient{margin-bottom:25px}
  .greeting{font-weight:bold;margin-bottom:6px}
  .letter-body p.para{margin-bottom:6px}
  .closing{position:absolute;left:38px;top:358px;font-size:5.4px;line-height:1.35}
  .signature{position:absolute;left:88px;top:352px;width:80px;height:30px;background:linear-gradient(90deg,rgba(60,70,150,.12),rgba(60,70,150,.04))}
  .letter-footer{position:absolute;left:38px;right:38px;top:485px;font-size:5.6px}
  .footer-name{font-weight:bold;margin-bottom:4px}
  .footer-rule{height:1px;background:#cfcfcf;margin-bottom:4px}
  .footer-line{display:flex;justify-content:space-between}
  .footer-web{font-weight:bold;font-size:6.2px}

  /* envelope front */
  .envelope-front{left:131px;top:660px;width:453px;height:195px}
  .envelope-front .header-band{height:28px}
  .envelope-front .wordmark{left:23px;top:55px;font-size:11px}
  .envelope-address{position:absolute;left:19px;top:173px;font-size:5.8px}
  .envelope-faint{position:absolute;right:14px;bottom:4px;font-size:26px;color:#dcdcdc;letter-spacing:.06em;text-transform:uppercase}

  /* envelope back */
  .envelope-back{left:615px;top:660px;width:451px;height:195px}
  .envelope-flap{position:absolute;left:0;top:0;width:100%;height:63px}
  .envelope-back .wordmark{left:0;right:0;top:30px;text-align:center;font-size:10px;color:var(--gold)}
  .envelope-web{position:absolute;left:0;right:0;top:167px;text-align:center;font-size:5.4px;color:#555}
</style>
</head>
<body>

<section class="piece folder" aria-label="Presentation folder">
  <div class="folder-spine"></div>
  <div class="wordmark">Copperfen Holdings</div>
</section>

<section class="piece letterhead" aria-label="Letterhead">
  <svg class="header-band" viewBox="0 0 404 30" preserveAspectRatio="none">
    <path d="M0 0H404V28Q200 4 0 12Z" fill="var(--charcoal)"/>
    <path d="M0 12Q200 4 404 28" stroke="var(--gold)" stroke-width="2.2" fill="none"/>
  </svg>
  <div class="wordmark">Copperfen Holdings Inc</div>

  <div class="letter-body">
    <div class="letter-date">30.09.2015</div>
    <div class="recipient">Recipient's name<br>Lindenweg 7<br>20412 Harlstadt<br>Germany</div>
    <div class="greeting">Dear sir,</div>
    <p class="para">Communication is a very integral part of living creatures, animals and humans. Communication may be verbal or written. Written communication however is only applicable to human beings. Can you even imagine a world without communication? Verbal communication can be through telephones, webcams or in person. Written communication is through letters, emails and mobile phone messages.</p>
    <p class="para">In today's world of great inventions and technology, letters have somehow become redundant. It is the time for text messages or chats. But they still can communicate a lot more than all other modes of communication. Organizations and various government departments still bank on letters as a strong medium of communication. There is no comparison in costs of sending letters as compared to costs of mobile phone messages though – letters are far cheaper. Letters now commonly known as "hard copy documents" are considered more relevant and important than email copies of text messages as proof or evidence of some sort.</p>
    <p class="para">Letters speak volumes about a person or an organization that writes it. So one must take utmost care ensuring that the language used in any letter is appropriate for the occasion for which it is being written. Since a letter is also a written proof or document, if there are certain things that should not form a part of it, then that too should be carefully handled.</p>
    <p class="para">Writing a good letter is an art. But if for some reason someone is unable to write that perfect letter, these different types of letters provide a base for you to build on. Sample letters have been given for everyone to understand what all information needs to form a part of the letter type and then it can be customized.</p>
  </div>
  <div class="closing">Yours Sincerely,<br><strong>Lena Vorholt</strong></div>
  <div class="signature" role="img" aria-label="Handwritten signature"></div>

  <footer class="letter-footer">
    <div class="footer-name">COPPERFEN HOLDINGS, INC.</div>
    <div class="footer-rule"></div>
    <div class="footer-line">
      <span>418 Alder Row; Suite 210 Marlow Falls, IA 50999</span>
      <span class="footer-web">www.copperfenholdings.com</span>
    </div>
  </footer>
</section>

<section class="piece envelope-front" aria-label="Envelope front">
  <svg class="header-band" viewBox="0 0 453 28" preserveAspectRatio="none">
    <path d="M0 0H453V27Q230 3 0 10Z" fill="var(--charcoal)"/>
    <path d="M0 10Q230 3 453 27" stroke="var(--gold)" stroke-width="2.2" fill="none"/>
  </svg>
  <div class="wordmark">Copperfen Holdings Inc</div>
  <div class="envelope-address">418 Alder Row; Suite 210 Marlow Falls, IA 50999</div>
  <div class="envelope-faint">Copperfen</div>
</section>

<section class="piece envelope-back" aria-label="Envelope back">
  <svg class="envelope-flap" viewBox="0 0 451 63" preserveAspectRatio="none">
    <path d="M0 0H451L437 60Q436 63 432 63H19Q15 63 14 60Z" fill="var(--charcoal)"/>
  </svg>
  <div class="wordmark">Copperfen Holdings</div>
  <div class="envelope-web">www.TallowBrookCA.com</div>
</section>

</body>
</html>
```